BRIGHT PEAK POWER.

I'd like my business logo.
contact name: Daniel Fitzhume
phone:0407395182
email: info@brightpeakpower.net.au
website: www.brightpeakpower.net.au

services:
solar
battery storage
LED lighting
energy saving solutions
general electrical
I'd like the design to look professional

Target Market(s)

Everyone

Industry/Entity Type

Business

Contact Information for Business Card

as described above

Requirements
Must have
• Id like the colours and the design to work well with my logo.

```html
<!DOCTYPE html>
<html lang="en">
<head>
<meta charset="utf-8">
<title>Bright Peak Power – Business Card</title>
<link rel="stylesheet" href="https://fonts.googleapis.com/css2?family=Lato:wght@400;700;900&display=swap">
<style>
  :root {
    --bg: #b9bec3;
    --card: #ffffff;
    --green: #8cc63f;
    --green-dark: #5fae2e;
    --orange: #f39c1e;
    --ink: #4d4d4f;
    --ink-soft: #58595b;
  }
  * { box-sizing: border-box; margin: 0; padding: 0; }
  html, body {
    width: 1200px; height: 1000px; overflow: hidden;
    background: var(--bg);
    font-family: "Lato", sans-serif;
  }
  .card {
    position: absolute;
    left: 150px; top: 245px;
    width: 900px; height: 510px;
    background: var(--card);
    box-shadow: 0 14px 40px rgba(0,0,0,0.22);
  }
  .brand {
    position: absolute;
    top: 78px; left: 0; right: 0;
    display: flex; align-items: center; justify-content: center; gap: 18px;
  }
  .brand-dot {
    width: 46px; height: 46px; border-radius: 50%;
    background: var(--orange);
  }
  .brand-name {
    font-weight: 900;
    font-size: 46px;
    letter-spacing: 1px;
    color: var(--green-dark);
  }
  .services {
    position: absolute;
    top: 198px; left: 0; right: 0;
    height: 36px;
    background: var(--green);
    color: #fff;
    font-weight: 700;
    font-size: 19px;
    letter-spacing: 1.4px;
    text-transform: uppercase;
    display: flex; align-items: center; justify-content: center;
    white-space: nowrap;
  }
  .services .sep { margin: 0 10px; }
  .person {
    position: absolute;
    left: 22px; top: 318px;
  }
  .person-name {
    font-weight: 700;
    font-size: 46px;
    color: var(--ink);
    line-height: 1;
  }
  .person-role {
    font-weight: 700;
    font-size: 21px;
    color: var(--green);
    margin-top: 6px;
  }
  .divider {
    position: absolute;
    left: 468px; top: 282px;
    width: 2px; height: 160px;
    background: var(--green);
  }
  .contacts {
    position: absolute;
    left: 492px; top: 282px;
    list-style: none;
  }
  .contacts li {
    display: flex; align-items: center; gap: 16px;
    height: 50px;
    font-size: 24px;
    color: var(--ink-soft);
  }
  .contacts svg { width: 32px; height: 32px; flex: none; }
</style>
</head>
<body>
  <article class="card">
    <header class="brand">
      <span class="brand-dot"></span>
      <span class="brand-name">BRIGHT PEAK POWER</span>
    </header>

    <div class="services">
      <span>Solar</span><span class="sep">|</span>
      <span>Battery Storage</span><span class="sep">|</span>
      <span>LED Lighting</span><span class="sep">|</span>
      <span>Energy Saving Solutions</span>
    </div>

    <section class="person">
      <h1 class="person-name">Daniel Fitzhume</h1>
      <p class="person-role">Director</p>
    </section>

    <div class="divider"></div>

    <ul class="contacts">
      <li>
        <svg viewBox="0 0 32 32" aria-hidden="true">
          <rect x="2" y="7" width="28" height="19" rx="1.5" fill="var(--orange)"/>
          <path d="M3 8 L16 18 L29 8" fill="none" stroke="#fff" stroke-width="2"/>
        </svg>
        <span>info@brightpeakpower.net.au</span>
      </li>
      <li>
        <svg viewBox="0 0 32 32" aria-hidden="true">
          <rect x="9" y="2" width="14" height="28" rx="2.5" fill="none" stroke="var(--orange)" stroke-width="2.4"/>
          <rect x="11.5" y="6" width="9" height="17" fill="var(--orange)"/>
          <circle cx="16" cy="26.5" r="1.4" fill="var(--orange)"/>
        </svg>
        <span>0407 395 182</span>
      </li>
      <li>
        <svg viewBox="0 0 32 32" aria-hidden="true">
          <g fill="none" stroke="var(--orange)" stroke-width="2.2">
            <circle cx="16" cy="16" r="13"/>
            <ellipse cx="16" cy="16" rx="6" ry="13"/>
            <line x1="3" y1="16" x2="29" y2="16"/>
            <path d="M5.5 9 H26.5 M5.5 23 H26.5"/>
          </g>
        </svg>
        <span>www.brightpeakpower.net.au</span>
      </li>
    </ul>
  </article>
</body>
</html>
```